Funhaven - launching a new children's entertainment venue

Create a flyer (to be used online and offline) to promote a new business

Business name (tbc). Current considerations are:
# "Bramblewood for KIDS"
# "BW for KIDS"
# "BW Parties"

Concept
# A creative play space for young children
# To be used for either (i) birthday parties or (ii) general play area available for Mums/parents groups to hire

Facilities:
# General play space
# Basketball, soccer
# Ball pit
# Video games
# Movies

Room designed for 2-8 year olds in mind

Catering available:
# Party pies, sausage rolls and mini franks
# Potato chips
# Cordial and water
Note - cake not included
Kitchen facility available.

Party host

Use of parents retreat room

Packages (costs):
# 2 hour party with catering pack and host $220 (up to 10 children, $17.50 per child for additional children)
# 2 hour party - BYO and host $200 (up to 10 children, $15 per child for additional children)
# Casual hire (exclusive use of room and parents retreat) - $50 per hour

Note - we also require a new logo for this new business concept

Existing business is called Bramblewood Sports, a basketball training and development facility. The new business needs to be linked to Bramblewood Sports from a banding perspective although does require its own identity

Brand essence - fun, vibrant, colourful, engaging
Updates

Project Deadline Extended Reason: Due to other projects we have been unable to review designs until tomorrow. Therefore we have opened deadline date. Added Monday, October 10, 2016

Target Market(s)

Mums of children aged 2-8 years

Industry/Entity Type

Entertainment

Logo Text

Name "Bramblewood for KIDS" (although name is not 100% confirmed)

Font styles to use
Serif
Sans Serif

Requirements
Must have
• Must be vibrant, colourful and fun
• Get across sense of energy
Nice to have
• Some sort of link to existing business "Bramblewood Sports" logos are attached
• Although we have an open mind to a totally seperate brand

```html
<!DOCTYPE html>
<html lang="en">
<head>
<meta charset="utf-8">
<title>Bramblewood for KIDS – Flyer</title>
<link href="https://fonts.googleapis.com/css2?family=Lilita+One&family=Gochi+Hand&family=Cabin:wght@400;500;600&display=swap" rel="stylesheet">
<style>
  :root {
    --page-bg: #ffffff;
    --cream: #f2f6dc;
    --orange-light: #fcc766;
    --orange: #f9a93e;
    --orange-deep: #f5921e;
    --blue: #1c74bc;
    --blue-light: #2f9ee0;
    --pink: #ec2a8a;
    --teal: #15a5a0;
    --ink: #1b1b1b;
  }
  * { margin: 0; padding: 0; box-sizing: border-box; }
  html, body { width: 1200px; height: 1200px; overflow: hidden; background: var(--page-bg); }
  .flyer {
    position: absolute; left: 159px; top: 30px;
    width: 881px; height: 1140px;
    background: var(--cream);
    overflow: hidden;
  }
  .kids-photo {
    position: absolute; left: 0; top: 430px; width: 499px; height: 710px;
    z-index: 0;
    background: linear-gradient(100deg, #f7e07a 0%, #f48a3a 32%, #8ccc4a 50%, #e8357a 70%, #3cc0e4 100%);
    border-top-right-radius: 160px;
  }
  .info-column {
    position: absolute; left: 499px; top: 0; width: 382px; height: 100%;
    z-index: 1;
    background: linear-gradient(90deg, var(--orange-light), var(--orange) 80%);
  }
  .info-column .edge-strip {
    position: absolute; right: 0; top: 0; width: 57px; height: 684px;
    background: var(--orange-deep);
  }
  .brand-rule { position: absolute; left: 47px; width: 410px; }
  .brand-rule.top { top: 59px; height: 11px; background: var(--orange); }
  .brand-rule.bottom { top: 274px; height: 11px; background: linear-gradient(90deg, var(--blue-light), var(--blue)); }
  .brand-name {
    position: absolute; left: 47px; top: 86px; width: 410px;
    font-family: "Lilita One", sans-serif; font-weight: 400; color: var(--blue);
    text-align: center; line-height: 0.98;
  }
  .brand-name .line-one { display: block; font-size: 68px; }
  .brand-name .line-two { display: block; font-size: 84px; }
  .tagline {
    position: absolute; left: 47px; top: 306px; width: 410px;
    font-family: "Gochi Hand", cursive; color: var(--blue);
    font-size: 40px; line-height: 1.15; text-align: center;
  }
  .section-heading {
    font-family: "Lilita One", sans-serif; font-weight: 400;
    line-height: 0.95; letter-spacing: 0.5px;
  }
  .facilities { position: absolute; left: 48px; top: 58px; }
  .facilities .section-heading { color: var(--blue); font-size: 48px; margin-bottom: 6px; }
  .facilities ul { list-style: none; font-family: "Cabin", sans-serif; font-weight: 500; font-size: 20px; color: var(--ink); }
  .facilities li { line-height: 28.5px; }
  .catering { position: absolute; left: 46px; top: 290px; width: 250px; }
  .catering .section-heading { color: var(--pink); font-size: 44px; margin-bottom: 6px; }
  .plain-list { list-style: none; font-family: "Cabin", sans-serif; font-weight: 400; color: var(--ink); }
  .catering .plain-list { font-size: 17px; line-height: 24px; }
  .plain-list li { padding-left: 14px; text-indent: -14px; }
  .plain-list li.note { padding-left: 12px; text-indent: 0; }
  .contact-band {
    position: absolute; left: 40px; top: 684px; width: 342px; height: 115px;
    background: linear-gradient(90deg, var(--blue-light), var(--blue));
    border-top-left-radius: 40px; border-bottom-left-radius: 40px;
    font-family: "Lilita One", sans-serif; color: #fff; text-align: center;
    padding-top: 26px;
  }
  .contact-band .phone { font-size: 26px; line-height: 34px; }
  .contact-band .web { font-size: 18px; line-height: 28px; }
  .packages { position: absolute; left: 56px; top: 830px; width: 290px; }
  .packages .section-heading { color: var(--teal); font-size: 44px; margin-bottom: 8px; }
  .packages .plain-list { font-size: 16.5px; line-height: 22.5px; }
</style>
</head>
<body>
<main class="flyer">
  <div class="kids-photo" role="img" aria-label="Photo of five smiling children in bright coloured t-shirts leaning in a row"></div>

  <div class="brand-rule top"></div>
  <h1 class="brand-name"><span class="line-one">Bramblewood</span><span class="line-two">for KIDS</span></h1>
  <div class="brand-rule bottom"></div>
  <p class="tagline">A creative play space<br>for young children</p>

  <section class="info-column">
    <div class="edge-strip"></div>
    <div class="facilities">
      <h2 class="section-heading">FACILITIES:</h2>
      <ul>
        <li>• General play space</li>
        <li>• Basketball &amp; soccer</li>
        <li>• Ball pit</li>
        <li>• Video games</li>
        <li>• Movies</li>
      </ul>
    </div>
    <div class="catering">
      <h2 class="section-heading">CATERING<br>AVAILABLE:</h2>
      <ul class="plain-list">
        <li>• Party pies, sausage rolls and mini franks</li>
        <li>• Potato chips</li>
        <li>• Cordial and water</li>
        <li class="note">Note - cake not included<br>Kitchen facility available.</li>
      </ul>
    </div>
    <div class="contact-band">
      <p class="phone">PHONE: 000-000-0000</p>
      <p class="web">WWW.BRAMBLEWOODFORKIDS.COM</p>
    </div>
    <div class="packages">
      <h2 class="section-heading">BIRTHDAY<br>PACKAGES:</h2>
      <ul class="plain-list">
        <li>• 2 hour party with catering pack and host $220 (up to 10 children, $17.50 per child for additional children)</li>
        <li>• 2 hour party - BYO and host $200 (up to 10 children, $15 per child for additional children)</li>
        <li>• Casual hire (exclusive use of room and parents retreat) - $50 per hour</li>
      </ul>
    </div>
  </section>
</main>
</body>
</html>
```